Identification Supplier website

Front and product page designs required for this Business Catalyst website for an identification supply company.

Also interested in coding same into finished site for additional fee.

Client is a security/event ID supplies company selling identification products like card holders, printers, lanyards, clips and so on.

Current placeholder site is at:
http://www.tagmorrow.com.au/

Other sites the client likes are at:

www.varrowdesigns.com.au

www.badgenook.com.au

www.qrv.com.au

http://start42.brimfield.co.nz/online/welcome.csn

Otherwise colour scheme should follow logo and structure should follow wireframe attached.

Industry/Entity Type

Business

```html
<!DOCTYPE html>
<html lang="en">
<head>
<meta charset="utf-8">
<title>Tagmorrow – ID Supplies</title>
<link href="https://fonts.googleapis.com/css2?family=Roboto+Condensed:wght@400;700&family=Roboto:wght@300;400&display=swap" rel="stylesheet">
<style>
  :root{
    --blue:#0a86c8;
    --blue-bright:#1a9ee0;
    --navy:#1d3557;
    --orange:#ef8a0c;
    --grey-dark:#66665c;
    --grey-panel:#a3a596;
    --grey-light:#c3c4b6;
    --text:#3a3a3a;
    --frame:#d6d6d0;
    --white:#ffffff;
  }
  *{box-sizing:border-box;margin:0;padding:0}
  html,body{width:1200px;height:900px;overflow:hidden;background:var(--white)}
  body{position:relative;font-family:"Roboto",Arial,sans-serif;color:var(--text)}
  .abs{position:absolute}

  .top-bar{left:0;top:0;width:1200px;height:35px;background:var(--blue);color:var(--white);font-size:11px}
  .top-bar .contact{position:absolute;right:162px;top:11px;display:flex;align-items:center;gap:6px}
  .top-bar .social{display:inline-block;width:15px;height:15px;border-radius:50%;background:#e6eef3;margin-left:2px}
  .top-bar .sep{margin:0 6px}

  .brand{left:161px;top:52px;display:flex;align-items:center;gap:8px;font-family:"Roboto",sans-serif;font-weight:400;font-size:32px;color:var(--navy);letter-spacing:.5px}
  .brand .mark{width:20px;height:20px;border-radius:50%;background:var(--blue)}

  .main-nav{left:625px;top:68px;display:flex;font-family:"Roboto Condensed",sans-serif;font-weight:700;font-size:13.5px;color:var(--navy)}
  .main-nav a{display:block;height:27px;line-height:27px;padding:0 9px;color:inherit;text-decoration:none}
  .main-nav a.active{background:var(--orange);color:var(--white);padding:0 14px;margin-right:2px}
  .main-nav a:last-child{padding-right:0}
  .header-rule{left:161px;top:105px;width:879px;height:2px;background:var(--blue)}

  .slider{left:161px;top:116px;width:630px;height:238px;background:linear-gradient(120deg,#cfc7c0,#e9e1da 45%,#b9b2ac)}
  .slider-dots{left:169px;top:343px;display:flex;gap:4px}
  .slider-dots span{width:23px;height:5px;background:var(--white)}
  .slider-dots span.on{background:var(--navy)}

  .section-head{height:33px;line-height:33px;padding-left:10px;color:var(--white);font-family:"Roboto Condensed",sans-serif;font-weight:700;font-size:13px;border-bottom:2px dashed rgba(255,255,255,.8)}
  .about-head{left:162px;top:364px;width:629px;background:var(--blue-bright)}
  .supplies-head{left:162px;top:555px;width:629px;background:var(--orange)}

  .about-img{left:162px;top:407px;width:129px;height:129px;border:4px solid #e2e2dc;background:linear-gradient(135deg,#e7eef3,#7fa9c9 60%,#3f7fb0)}
  .about-text{left:301px;top:408px;width:488px;font-size:10.4px;line-height:16.7px;letter-spacing:.1px;text-align:justify;font-weight:400}

  .product{width:142px;height:122px;border:1px solid var(--frame);background:var(--white)}
  .product .photo{height:94px}
  .product .label{position:absolute;left:5px;bottom:6px;display:flex;align-items:center;gap:5px;font-family:"Roboto Condensed",sans-serif;font-weight:700;font-size:11px;color:var(--blue)}
  .product .label i{display:inline-block;width:13px;height:13px;background:var(--orange);position:relative}
  .product .label i::after{content:"";position:absolute;left:5px;top:3.5px;border-left:4px solid var(--white);border-top:3px solid transparent;border-bottom:3px solid transparent}

  .news-panel{left:800px;top:116px;width:240px;height:280px;background:var(--grey-panel)}
  .news-panel .panel-head{height:33px;background:var(--grey-dark);border-bottom:2px dashed #c9c9bd;color:var(--white);font-family:"Roboto Condensed",sans-serif;font-weight:700;font-size:12.5px;display:flex;align-items:center;padding-left:14px;gap:8px}
  .news-item{margin:0 10px 0 15px;border-bottom:1px solid #c4c6b9;padding:10px 0 2px}
  .news-item:first-of-type{margin-top:6px}
  .news-item h4{font-weight:400;font-size:12px;color:#e5f6ff}
  .news-item p{font-size:10.2px;color:var(--white);margin-top:1px}
  .news-item.last{border-bottom:none}
  .news-panel .more{position:absolute;right:10px;bottom:14px;font-size:10px;color:var(--white)}

  .newsletter{left:801px;top:402px;width:238px;height:60px;background:linear-gradient(#2aa6e6,#1287cd);color:var(--white)}
  .newsletter .small{position:absolute;left:73px;top:12px;font-size:11px;color:var(--navy)}
  .newsletter .big{position:absolute;left:74px;top:24px;font-family:"Roboto Condensed",sans-serif;font-size:23px;letter-spacing:.5px}
  .newsletter svg{position:absolute;left:26px;top:18px}

  .featured-head{left:801px;top:469px;width:238px;height:33px;line-height:33px;background:var(--grey-light);padding-left:10px;color:var(--white);font-family:"Roboto Condensed",sans-serif;font-weight:700;font-size:13px;border-bottom:2px solid #e4e4da}
  .featured-img{left:801px;top:504px;width:238px;height:137px;border:4px solid #e8e8e0;background:radial-gradient(circle at 60% 50%,#fff4a8,#f5cf3a 70%,#e9b81e)}
  .featured-text{left:803px;top:647px;width:236px;font-size:10px;line-height:16.8px;letter-spacing:-.1px;font-weight:300;color:#333}

  .footer{left:0;top:857px;width:1200px;height:43px;background:var(--blue);color:var(--white);font-size:11px;font-weight:300}
  .footer nav{position:absolute;left:162px;top:10px;display:flex}
  .footer nav span{margin:0 6px}
  .footer .copy{position:absolute;right:161px;top:10px}
</style>
</head>
<body>

<header>
  <div class="abs top-bar">
    <div class="contact">
      <svg width="14" height="14" viewBox="0 0 14 14"><path d="M3 1l2 3-1.3 1.3a8 8 0 0 0 5 5L10 9l3 2-1 2.5C6 13 1 8 .7 2z" fill="#fff"/></svg>
      <span>03-9018 2276</span><span class="sep">|</span><span>Follow us on</span>
      <span class="social" aria-label="Social link"></span><span class="social" aria-label="Social link"></span><span class="social" aria-label="Feed link"></span>
    </div>
  </div>

  <div class="abs brand"><span class="mark"></span>tagmorrow</div>

  <nav class="abs main-nav">
    <a class="active">HOME</a><a>ABOUT US</a><a>PRODUCTS</a><a>SUPPORT</a><a>CONTACT US</a><a>NEWS</a>
  </nav>
  <div class="abs header-rule"></div>
</header>

<main>
  <div class="abs slider" role="img" aria-label="Woman holding up a printed student ID card in an office"></div>
  <div class="abs slider-dots"><span class="on"></span><span></span><span></span><span></span></div>

  <h2 class="abs section-head about-head">WHAT IS TAGMORROW</h2>
  <div class="abs about-img" role="img" aria-label="Photo ID badge cards"></div>
  <p class="abs about-text">Yes, We mean everything.<br>From membership cards...to the latest holographic effect ID badges for the most security sensitive organisations. And as the ID specialist we'll even help you with advice on the design and printing of your customised membership or ID cards as well as specifications to suit your budget. With access to more than 3,500 items to choose from (minimum quantities &amp; availability may apply), plus a large range of equipment, supplies &amp; accessories, there is a cost effective system or solution to suit your needs.Your no-risk unconditional guarantee of quality products is shared by numerous clubs, hospitals, libaries, schools, colleges, companies, associations &amp; government departments.</p>

  <h2 class="abs section-head supplies-head">EVERYTHING YOU WILL EVER NEED IN ID SUPPLIES....</h2>

  <div class="abs product" style="left:162px;top:595px"><div class="photo" role="img" aria-label="Card printer ribbons and cartridges" style="background:linear-gradient(#fff 10%,#6f8fb8 50%,#2b3f66 80%,#fff)"></div><div class="label"><i></i>CARD PRINTERS</div></div>
  <div class="abs product" style="left:327px;top:595px"><div class="photo" role="img" aria-label="Card holders" style="background:linear-gradient(120deg,#fff 15%,#3a3a3a 35%,#505050 60%,#f3588a 75%,#fff)"></div><div class="label"><i></i>CARDHOLDERS</div></div>
  <div class="abs product" style="left:490px;top:595px"><div class="photo" role="img" aria-label="Man working at a computer" style="background:linear-gradient(120deg,#8c8c88,#d8d8d4 50%,#f5f5f3)"></div><div class="label"><i></i>BUREAU SERVICES</div></div>
  <div class="abs product" style="left:649px;top:595px"><div class="photo" role="img" aria-label="Printed lanyards" style="background:linear-gradient(160deg,#fff 20%,#d8575a 40%,#5a8ed0 55%,#e9e9e9 75%,#fff)"></div><div class="label"><i></i>LANYARDS</div></div>

  <div class="abs product" style="left:162px;top:722px"><div class="photo" role="img" aria-label="Coloured binder clips" style="background:linear-gradient(160deg,#fff 15%,#5a59c8 35%,#f0d11e 50%,#d2312b 65%,#fff 85%)"></div><div class="label"><i></i>CLIPS</div></div>
  <div class="abs product" style="left:327px;top:722px"><div class="photo" role="img" aria-label="Coloured silicone wristbands" style="background:linear-gradient(90deg,#e84a4a,#f39b2a 30%,#5aa0e8 60%,#c36fd8 85%,#f0f0f0)"></div><div class="label"><i></i>WRISTBANDS</div></div>
  <div class="abs product" style="left:490px;top:722px"><div class="photo" role="img" aria-label="Slot punch tool" style="background:radial-gradient(circle at 55% 55%,#5a5a5a,#bdbdbd 45%,#fff 70%)"></div><div class="label"><i></i>SLOT PUNCHES</div></div>
  <div class="abs product" style="left:649px;top:722px"><div class="photo" role="img" aria-label="Printer ribbon rolls" style="background:linear-gradient(90deg,#d3396b,#c9b23a 35%,#2f8f5a 65%,#9b2a4a)"></div><div class="label"><i></i>ACCESSORIES</div></div>
</main>

<aside>
  <section class="abs news-panel">
    <div class="panel-head">
      <svg width="18" height="18" viewBox="0 0 18 18"><path d="M2 1h8l4 4v11H2z" fill="none" stroke="#fff" stroke-width="1.6"/><path d="M13 10v7M9.5 13.5h7" stroke="#fff" stroke-width="2"/></svg>
      WHAT'S NEW !
    </div>
    <div class="news-item"><h4>Lorem Ipsum</h4><p>s simply dummy text of the printing and types</p></div>
    <div class="news-item"><h4>Lorem Ipsum</h4><p>s simply dummy text of the printing and types</p></div>
    <div class="news-item"><h4>Lorem Ipsum</h4><p>s simply dummy text of the printing and types</p></div>
    <div class="news-item last"><h4>Lorem Ipsum</h4><p>s simply dummy text of the printing and types</p></div>
    <span class="more">More..</span>
  </section>

  <section class="abs newsletter">
    <svg width="34" height="24" viewBox="0 0 34 24"><rect x="1.5" y="1.5" width="31" height="21" rx="3" fill="none" stroke="#f0a020" stroke-width="2.5"/><path d="M3 4l14 10 14-10M3 20l10-8M31 20l-10-8" fill="none" stroke="#f0a020" stroke-width="2"/></svg>
    <span class="small">Sign Up to Receive&nbsp; Our Free</span>
    <span class="big">NEWS LETTER</span>
  </section>

  <h3 class="abs featured-head">FEATURED PRODUCT</h3>
  <div class="abs featured-img" role="img" aria-label="Black and green business cards on a yellow background"></div>
  <p class="abs featured-text">Lorem Ipsum is simply dummy text of the printing and typesetting industry. Lorem Ipsum has been the industry's standard dummy text ever since the 1500s, when an unknown printer took a galley of type and scrambled it to make a type specimen book. It has survived not only five centuries, but also the leap into</p>
</aside>

<footer class="abs footer">
  <nav>Home<span>|</span>About Us<span>|</span>Products<span>|</span>Support<span>|</span>Contact Us<span>|</span>News</nav>
  <div class="copy">Copyright©tagmorrow.com.au. All Rights Reserved.</div>
</footer>

</body>
</html>
```